Need a professional looking Consulting site for Consulting Services Company

Stock professional office images with a registration page for contact

Coding

Coded - Design and coding required

```html
<!DOCTYPE html>
<html lang="en">
<head>
<meta charset="UTF-8">
<title>Verdaway Consulting</title>
<link href="https://fonts.googleapis.com/css2?family=Open+Sans:wght@300;400&display=swap" rel="stylesheet">
<style>
  :root {
    --leaf: #7aaa46;
    --leaf-dark: #4f8a2e;
    --paper: #ffffff;
    --field-text: #5c6670;
  }
  * { box-sizing: border-box; margin: 0; padding: 0; }
  html, body { width: 723px; height: 1200px; overflow: hidden; background: var(--paper); }
  body { position: relative; font-family: "Open Sans", Arial, sans-serif; }
  .shapes { position: absolute; inset: 0; }
  .registration-form { position: absolute; left: 12px; top: 116px; width: 315px; }
  .field {
    background: var(--paper);
    color: var(--field-text);
    font-size: 10px;
    padding: 0 8px;
    border-bottom: 1px solid var(--leaf);
    margin-bottom: 16px;
  }
  .field-line { height: 24px; line-height: 24px; }
  .field-area { height: 100px; padding-top: 5px; }
  .register-button {
    position: absolute; left: 277px; top: 312px;
    width: 50px; height: 50px; border-radius: 50%;
    background: var(--leaf); color: var(--paper);
    font-size: 10.5px; line-height: 50px; text-align: center;
  }
  .brand-name {
    position: absolute; left: 457px; top: 196px; width: 194px;
    text-align: center; font-size: 33px; font-weight: 400;
    color: var(--leaf-dark); letter-spacing: -0.5px; line-height: 1;
  }
  .feature { position: absolute; color: var(--paper); }
  .feature h2 { font-weight: 400; line-height: 1.18; }
  .feature p { font-weight: 300; font-size: 10.6px; line-height: 18.5px; }
  .feature-growth { left: 434px; top: 489px; width: 202px; }
  .feature-growth h2 { font-size: 21px; margin-bottom: 28px; }
  .feature-advantage { left: 103px; top: 874px; width: 220px; }
  .feature-advantage h2 { font-size: 25px; margin-bottom: 28px; }
</style>
</head>
<body>
<svg class="shapes" width="723" height="1200" viewBox="0 0 723 1200">
  <defs>
    <linearGradient id="office-team" x1="0" y1="0" x2="1" y2="1">
      <stop offset="0" stop-color="#4a7fb8"/>
      <stop offset="0.35" stop-color="#6fa640"/>
      <stop offset="0.6" stop-color="#d6d98a"/>
      <stop offset="1" stop-color="#3f7a2a"/>
    </linearGradient>
    <linearGradient id="skyline" x1="0" y1="0" x2="0" y2="1">
      <stop offset="0" stop-color="#e4f2f3"/>
      <stop offset="0.55" stop-color="#6fb8c0"/>
      <stop offset="0.8" stop-color="#c9b9a0"/>
      <stop offset="1" stop-color="#4c4036"/>
    </linearGradient>
    <linearGradient id="lobby" x1="0" y1="0" x2="0" y2="1">
      <stop offset="0" stop-color="#f7f8f4"/>
      <stop offset="0.5" stop-color="#7e9a5e"/>
      <stop offset="1" stop-color="#6b5a4d"/>
    </linearGradient>
    <linearGradient id="desk" x1="0" y1="0" x2="0" y2="1">
      <stop offset="0" stop-color="#4f6f30"/>
      <stop offset="0.45" stop-color="#8a6a45"/>
      <stop offset="0.7" stop-color="#8fa160"/>
      <stop offset="1" stop-color="#e6e6e4"/>
    </linearGradient>
    <linearGradient id="consultant" x1="0" y1="0" x2="0" y2="1">
      <stop offset="0" stop-color="#f2f3f0"/>
      <stop offset="0.35" stop-color="#9bae86"/>
      <stop offset="0.6" stop-color="#e3c2a8"/>
      <stop offset="1" stop-color="#7a5140"/>
    </linearGradient>
    <clipPath id="badge-clip"><circle cx="553" cy="212" r="116"/></clipPath>
  </defs>

  <rect class="top-band" x="0" y="0" width="595" height="19" fill="var(--leaf)"/>
  <polygon role="img" aria-label="Consultants reviewing documents together in a bright modern office"
           points="0,26 595,26 529,401 0,401" fill="url(#office-team)"/>

  <circle cx="553" cy="212" r="117" fill="var(--leaf)"/>
  <rect role="img" aria-label="Calm city skyline seen through an office window"
        x="437" y="96" width="232" height="232" fill="url(#skyline)" clip-path="url(#badge-clip)"/>

  <rect class="divider-band" x="0" y="408" width="714" height="8" fill="var(--leaf)"/>

  <polygon role="img" aria-label="Office lobby with tall potted plants against a white wall"
           points="76,442 202,442 202,803 27,803" fill="url(#lobby)"/>
  <polygon role="img" aria-label="Wooden office desk with laptop, notebook and coffee cup"
           points="207,442 382,442 333,803 207,803" fill="url(#desk)"/>
  <polygon class="panel" points="407,442 714,442 665,803 357,803" fill="var(--leaf)"/>

  <polygon class="panel" points="26,829 333,829 382,1188 75,1188" fill="var(--leaf)"/>
  <polygon role="img" aria-label="Business consultant in a white shirt working at a laptop by a window"
           points="357,829 665,829 714,1188 406,1188" fill="url(#consultant)"/>
</svg>

<form class="registration-form" aria-label="Registration">
  <div class="field field-line">Name</div>
  <div class="field field-line">Email</div>
  <div class="field field-area">Message</div>
</form>
<div class="register-button">Register</div>

<div class="brand-name">Verdaway</div>

<section class="feature feature-growth">
  <h2>Strategy: The growth plan</h2>
  <p>As markets shift faster every quarter and missed chances cost firms millions each year, many leaders are finding their way forward with expert advisors, to sharpen strategy and curb wasted spend.</p>
</section>

<section class="feature feature-advantage">
  <h2>The consulting advantage</h2>
  <p>According to our 2016 client survey, firms that work with outside advisors are more effective in reaching most types of growth goals. Thanks to clear frameworks, proven methods that cut through noise between the boardroom and the team, consulting is poised to become a powerful ally in success.</p>
</section>
</body>
</html>
```